Menstrual cramp drink product needs a packaging design

We need a packaging design for our start-up Marigane. Marigane makes a menstrual cramp relief product based on Chinese medicine. The product is an herbal powder dissolved in water and will be sold online in the US, targeted towards 22-35 year old women. There are 14 herbs in it (see below).

The product is drank twice a day. Once in morning and once in the evening. The powder is about 6 grams and the consumer will dissolve it in water in a shot glass. Consumer will drink it quickly. Packaging can have a "AM" and a "PM" version to help consumers remember when to take them.

We want our consumers to think of packaging as an experience! Packaging means two things:

1. Aluminum sealed sachet (think tea) that prevents water from coming in. We want to make it fun, so ways to make it stand out is to make it circular (like a period) or to make it like a bubble so that consumer can "pop" it out into the glass.

Measurement: 2.5 x 2.5 inches (able to fit in that space)

*Have a front and back design. Leave room in the back for "supplement fact." Look at Verdant pim packaging: https://www.verdantpim.example/product/digestive-support-soothing/

2. Cardboard box front, 2 sides, back - measurement: 2.6 x 2.6 x 3.6 inches

We have attached our logo, so that you can incorporate it into the packaging. We like the mint/indigo color combination of LUMREN skincare products: https://www.lumren.example/shop-our-products/face/cleansing-oil#?offset=0&limit=24

On 1 side - please include the 14 herbs in our product; would love for a side of the outer box packaging to have images of all the herbs in order to show transparency. The other side can be word filler for now (will most likely become directions to take the product)
Updates

Exta guidance:-Packaging colors and design need to stand out in a crowded aisle of supplements. Can't look very "busy" and needs to look minimalist and higher end-I would ask you to use bolder colorblocking like LUMREN skincare and Quarry of Brews Stay Bright/Fresh line. We don't need to stick to the logo colors only. I imagine packaging to be a lot more colorful (kind of like India's Holi festival). Use of bright gold, orange, burgundy, etc is all welcome to give the idea that the product is letting a woman CELEBRATE her womanhood!-We want the consumer to get a sense of fun and vivaciousness (not yoga zen)-There will be ten small packages inside (5 morning and 5 evening) - AM and PM packets are the same, but perhaps the colors can be different for both as an extra reminder to take it.Please look at VORELI skincare products for packaging inspiration. I like their minimalist, detail-oriented, modern, and clean feel. Added Monday, October 24, 2016

Target Market(s)

22-35 year old women - USA

Industry/Entity Type

Product

Requirements
Must have
• Pictures of each of the ingredient - modern, clean-looking
• English & Chinese name:
• Chai Hu/Bupleurum
• Chi Shao/Red Peony
• Zi Ke or Zi Qiao /Bitter Orange Peel
• Xiang Fu/Cyperus
• Chuan Xiong/Ligusticum
• Hu Tao Ren/Peach Kernel
• Hong Hua/Carthamus
• Yan Hu Suo/Corydalis
• Dang Gui
• Ai Ye/Artemisia Argyi (Mugwort leaf)
• Gan Cao/Licorice
• Seasonings:
• Chen Pi (Orange or Citrus Peel)
• Sheng jiang/Fresh ginger rhizome
• Hong tang/Brown sugar

```html
<!DOCTYPE html>
<html lang="en">
<head>
<meta charset="utf-8">
<title>Marigane Herbal Drink PM Label</title>
<link rel="stylesheet" href="https://fonts.googleapis.com/css2?family=Oswald:wght@300;500;600&display=swap">
<style>
  :root {
    --stage: #ededed;
    --paper: #ffffff;
    --forest: #123019;
    --forest-mid: #2b5a22;
    --mint: #8fd1a8;
    --sun: #fde01a;
    --lemon: #f5ef72;
    --lemon-pale: #fbf79a;
    --lime: #d6df2a;
    --leaf: #9cc43a;
    --leaf-light: #cfe86c;
    --leaf-mid: #b5df72;
    --moss: #7fb040;
    --amber: #fbb81c;
    --cream: #fff4c4;
    --magenta: #e8068c;
    --ink: #111111;
  }
  html, body {
    margin: 0;
    width: 1200px;
    height: 907px;
    overflow: hidden;
    background: var(--stage);
  }
  .label {
    position: absolute;
    left: 356px;
    top: 212px;
    width: 484px;
    height: 484px;
    display: block;
  }
  .brand-name {
    font-family: "Oswald", sans-serif;
    font-weight: 600;
    fill: var(--forest);
  }
  .product-title {
    font-family: "Oswald", sans-serif;
    font-weight: 500;
    fill: var(--paper);
  }
  .product-subtitle {
    font-family: "Oswald", sans-serif;
    font-weight: 300;
    fill: var(--paper);
  }
  .dose-mark {
    font-family: "Oswald", sans-serif;
    font-weight: 600;
    fill: var(--paper);
  }
  .net-weight {
    font-family: "Oswald", sans-serif;
    fill: var(--ink);
  }
</style>
</head>
<body>
<svg class="label" viewBox="0 0 605 605" xmlns="http://www.w3.org/2000/svg">
  <defs>
    <clipPath id="label-edge"><rect width="605" height="605"/></clipPath>
    <radialGradient id="banner-fill" cx="0.45" cy="0.5" r="0.6">
      <stop offset="0" stop-color="#2b5a22"/>
      <stop offset="1" stop-color="#123019"/>
    </radialGradient>
    <radialGradient id="herb-fill" cx="0.5" cy="0.55" r="0.5">
      <stop offset="0" stop-color="#8a9a2a" stop-opacity="0.35"/>
      <stop offset="0.7" stop-color="#a8b33a" stop-opacity="0.18"/>
      <stop offset="1" stop-color="#a8b33a" stop-opacity="0"/>
    </radialGradient>
  </defs>

  <g clip-path="url(#label-edge)">
    <!-- colour blocks -->
    <rect class="block-sun" width="605" height="605" fill="var(--sun)"/>
    <path class="block-lemon" d="M0 0 H605 V460 H90 Q10 440 0 330 Z" fill="var(--lemon)"/>
    <circle class="block-lime-right" cx="650" cy="420" r="150" fill="var(--lime)"/>
    <circle class="block-glow" cx="455" cy="270" r="110" fill="var(--lemon-pale)" opacity="0.85"/>
    <rect class="block-lime" x="0" y="455" width="605" height="150" fill="var(--lime)"/>
    <circle class="disc-large" cx="230" cy="605" r="130" fill="var(--leaf-light)"/>
    <circle class="disc-small" cx="232" cy="500" r="42" fill="var(--leaf)"/>
    <circle class="disc-right" cx="490" cy="610" r="125" fill="var(--moss)"/>
    <circle class="disc-right-inner" cx="455" cy="570" r="68" fill="var(--leaf-mid)"/>

    <!-- header -->
    <path class="header-band" d="M0 0 H605 V140 Q470 170 360 180 Q160 190 0 20 Z" fill="var(--paper)"/>
    <path class="header-rule" d="M0 20 Q160 190 360 180 Q470 170 605 135 L605 158 Q470 183 360 188 Q150 195 0 35 Z" fill="var(--forest)"/>

    <!-- brand -->
    <circle class="brand-dot" cx="187" cy="73" r="48" fill="var(--mint)"/>
    <text class="brand-name" x="244" y="100" font-size="64" textLength="224" lengthAdjust="spacingAndGlyphs">Marigane</text>

    <!-- herb artwork -->
    <ellipse class="herb-art" cx="380" cy="320" rx="230" ry="110" fill="url(#herb-fill)" role="img" aria-label="Line drawing of assorted herbs: mint, leafy sprigs, grasses and fennel flowers"/>

    <!-- natural quality seal -->
    <g class="quality-seal">
      <circle cx="513" cy="211" r="74" fill="var(--cream)"/>
      <circle cx="513" cy="211" r="70" fill="none" stroke="var(--amber)" stroke-width="3"/>
      <circle cx="513" cy="211" r="44" fill="var(--amber)"/>
    </g>

    <!-- title banner -->
    <path class="title-banner" d="M70 343 H470 Q520 343 530 400 L535 453 H115 Q90 453 82 420 Z" fill="url(#banner-fill)"/>
    <text class="product-title" x="128" y="413" font-size="64" textLength="330" lengthAdjust="spacingAndGlyphs">HERBAL DRINK</text>
    <text class="product-subtitle" x="460" y="437" font-size="20" text-anchor="end" textLength="194" lengthAdjust="spacingAndGlyphs">MENSTRUAL CRAMP RELIEF</text>

    <!-- dose marker -->
    <circle class="dose-badge" cx="498" cy="480" r="46" fill="var(--magenta)" stroke="var(--ink)" stroke-width="4"/>
    <text class="dose-mark" x="498" y="500" font-size="52" text-anchor="middle">PM</text>

    <!-- net weight -->
    <text class="net-weight" x="20" y="587" font-size="32"><tspan font-weight="600">25G</tspan><tspan font-weight="300" font-size="23"> (0.9 OZ)</tspan></text>
  </g>
  <rect width="605" height="605" fill="none" stroke="#9a9a9a" stroke-width="1"/>
</svg>
</body>
</html>
```